Business cards to launch an education platform

Hi,
I am looking at having new business cards designed.
I am a startup, developing a web platform for schools and university, the education world. It's an online assessment system.
I would like a card that looks classy, and that is using the colors and the font of my logo.

I have attached:
1) my logo
2) A business card that I have designed quickly so you can have all the information required in the card, but I really don't like it.
3) The font that I am using (Lato Regular) to design my web platform
4) Some screenshots of my web platform so you can have a look at the style that I have.

Target Market(s)

Major market: Education system: Schools and university
Minor markets: Business in general

Industry/Entity Type

Business

Contact Information for Business Card

Tessa Vinall
Director

M: 0487 312 950
E: tessa.vinall@copperLoomVentures.com.au

Requirements
Must have
• The colors of my logo

```html
<!DOCTYPE html>
<html lang="en">
<head>
<meta charset="utf-8">
<title>Copper Loom Ventures – Business Cards</title>
<link rel="stylesheet" href="https://fonts.googleapis.com/css2?family=Exo+2:wght@400;500;600&display=swap">
<style>
  :root {
    --backdrop: #d6cec5;
    --card-white: #ffffff;
    --brand-blue: #1f7fcc;
    --panel-top: #2f9be0;
    --panel-bottom: #1463b3;
    --stripe: #5cc3ef;
    --text-white: #ffffff;
    --name-blue: #2a86c9;
  }
  * { margin: 0; padding: 0; box-sizing: border-box; }
  html, body { width: 1200px; height: 745px; overflow: hidden; }
  body {
    background: var(--backdrop);
    font-family: "Exo 2", Arial, sans-serif;
    position: relative;
  }
  .card {
    position: absolute;
    top: 220px;
    width: 487px;
    height: 281px;
    background: var(--card-white);
    overflow: hidden;
  }
  .card-front { left: 97px; }
  .card-back { left: 594px; }

  .front-divider {
    position: absolute;
    left: 0; top: 0;
    width: 487px; height: 281px;
  }

  .brand {
    position: absolute;
    display: flex;
    align-items: center;
    gap: 9px;
  }
  .brand-square {
    width: 40px; height: 40px;
    background: var(--brand-blue);
    flex: none;
  }
  .brand-name {
    color: var(--name-blue);
    font-weight: 500;
    font-size: 17px;
    line-height: 1.1;
    letter-spacing: 0.5px;
  }
  .card-front .brand { left: 24px; top: 122px; }
  .card-back .brand { left: 50%; top: 50%; transform: translate(-50%, -50%); }
  .card-back .brand-square { width: 52px; height: 52px; }
  .card-back .brand-name { font-size: 21px; }

  .holder {
    position: absolute;
    left: 276px; top: 52px;
    color: var(--text-white);
  }
  .holder-name {
    font-size: 15px;
    font-weight: 500;
    letter-spacing: 0.6px;
    text-transform: uppercase;
  }
  .holder-role {
    font-size: 7px;
    letter-spacing: 0.6px;
    text-transform: uppercase;
    margin-left: 26px;
    margin-top: 1px;
  }

  .contacts {
    position: absolute;
    left: 266px; top: 138px;
    list-style: none;
    color: var(--text-white);
  }
  .contacts li {
    display: flex;
    align-items: center;
    gap: 6px;
    height: 20px;
    font-size: 13px;
    letter-spacing: 0.4px;
    white-space: nowrap;
  }
  .contacts li.small { font-size: 10px; letter-spacing: 0.1px; }
  .contacts li.tiny { font-size: 8px; }
  .contact-icon { width: 13px; height: 13px; flex: none; }
</style>
</head>
<body>

<section class="card card-front" aria-label="Business card front">
  <svg class="front-divider" viewBox="0 0 487 281" aria-hidden="true">
    <defs>
      <linearGradient id="panelShade" x1="0" y1="0" x2="0" y2="1">
        <stop offset="0" stop-color="var(--panel-top)"/>
        <stop offset="1" stop-color="var(--panel-bottom)"/>
      </linearGradient>
    </defs>
    <path d="M256 0 H487 V281 H256 V82 Q256 76 262 72 L268 68 Q272 65 268 61 L262 56 Q256 52 256 46 Z" fill="url(#panelShade)"/>
    <path d="M250 0 V46 Q250 54 257 58 L262 62 Q265 65 262 68 L257 72 Q250 76 250 84 V281" fill="none" stroke="var(--stripe)" stroke-width="4"/>
  </svg>

  <div class="brand">
    <span class="brand-square"></span>
    <span class="brand-name">Copper Loom<br>Ventures</span>
  </div>

  <div class="holder">
    <p class="holder-name">Tessa Vinall</p>
    <p class="holder-role">General Manager</p>
  </div>

  <ul class="contacts">
    <li>
      <svg class="contact-icon" viewBox="0 0 14 14" aria-hidden="true"><circle cx="7" cy="7" r="7" fill="#fff"/><rect x="5" y="3" width="4" height="8" rx="1" fill="none" stroke="#1f7fcc" stroke-width="1.2"/></svg>
      0487 312 950
    </li>
    <li>
      <svg class="contact-icon" viewBox="0 0 14 14" aria-hidden="true"><circle cx="7" cy="7" r="7" fill="#fff"/><path d="M4.5 3.5 L6 3.5 L6.5 5.5 L5.6 6.3 Q6.5 8 7.8 8.6 L8.6 7.6 L10.5 8.1 L10.5 9.6 Q7.5 10 5.5 8 Q3.8 6 4.5 3.5 Z" fill="#1f7fcc"/></svg>
      0487 312 950
    </li>
    <li class="small">
      <svg class="contact-icon" viewBox="0 0 14 14" aria-hidden="true"><circle cx="7" cy="7" r="7" fill="#fff"/><rect x="3.5" y="4.5" width="7" height="5" fill="none" stroke="#1f7fcc" stroke-width="1"/><path d="M3.5 4.5 L7 7.5 L10.5 4.5" fill="none" stroke="#1f7fcc" stroke-width="1"/></svg>
      tessa.vinall@copperLoomVentures.com.au
    </li>
    <li class="small">
      <svg class="contact-icon" viewBox="0 0 14 14" aria-hidden="true"><circle cx="7" cy="7" r="7" fill="#fff"/><circle cx="7" cy="7" r="3.6" fill="none" stroke="#1f7fcc" stroke-width="1"/><path d="M3.4 7 H10.6 M7 3.4 Q5 7 7 10.6 M7 3.4 Q9 7 7 10.6" fill="none" stroke="#1f7fcc" stroke-width="0.8"/></svg>
      copperLoomVentures.com.au
    </li>
    <li class="tiny">
      <svg class="contact-icon" viewBox="0 0 14 14" aria-hidden="true"><circle cx="7" cy="7" r="7" fill="#fff"/><path d="M7 11 Q4 7.5 4 6 A3 3 0 0 1 10 6 Q10 7.5 7 11 Z" fill="#1f7fcc"/><circle cx="7" cy="6" r="1.1" fill="#fff"/></svg>
      12 Harlow Lane, Level 3, Fitzroy VIC
    </li>
  </ul>
</section>

<section class="card card-back" aria-label="Business card back">
  <div class="brand">
    <span class="brand-square"></span>
    <span class="brand-name">Copper Loom<br>Ventures</span>
  </div>
</section>

</body>
</html>
```